Business Card for a Wedding Films Business

We require a business card design for our business 'Lewis Marrow Wedding Films'. The logo needs to look classy and high end.

Target Market(s)

Wedding Couples

Contact Information for Business Card

Lewis Marrow Wedding Films
07312 605 227
films@lewismarrowreels.com
www.lewismarrowreels.com

Facebook: @lewismarrowweddingfilms
Instagram: @lewismarrowfilms

Font styles to use
Sans Serif

Requirements
Must have
• Social media icons - Facebook and Instagram

```html
<!DOCTYPE html>
<html lang="en">
<head>
<meta charset="utf-8">
<title>Lewis Marrow Wedding Films – Business Card</title>
<link rel="stylesheet" href="https://fonts.googleapis.com/css2?family=Jost:wght@400;500&family=Roboto:wght@400;500;700&display=swap">
<style>
  :root {
    --backdrop: #c8c8c8;
    --card-dark: #2f3235;
    --card-light: #f2f2f2;
    --gold: #8d6a2c;
    --ink: #2b2b2b;
    --white: #ffffff;
  }
  * { margin: 0; padding: 0; box-sizing: border-box; }
  html, body {
    width: 1200px;
    height: 576px;
    overflow: hidden;
    background: var(--backdrop);
  }
  .canvas {
    position: relative;
    width: 1200px;
    height: 576px;
  }
  .card {
    position: absolute;
    width: 484px;
    height: 292px;
    border-radius: 12px;
    overflow: hidden;
  }
  .card--front {
    left: 82px;
    top: 139px;
    background: var(--card-dark);
  }
  .card--back {
    left: 602px;
    top: 138px;
    background: var(--card-light);
  }

  /* Wordmark */
  .wordmark {
    position: absolute;
    text-align: center;
    font-family: "Jost", sans-serif;
    font-weight: 400;
    text-transform: uppercase;
    line-height: 1;
  }
  .wordmark__dot {
    display: block;
    margin: 0 auto 14px;
    border-radius: 50%;
  }
  .wordmark__name { display: block; white-space: nowrap; }
  .wordmark__tag { display: block; white-space: nowrap; }

  .card--front .wordmark {
    left: 0; right: 0; top: 118px;
    color: var(--white);
  }
  .card--front .wordmark__dot {
    width: 12px; height: 12px;
    background: var(--white);
  }
  .card--front .wordmark__name {
    font-size: 25px;
    letter-spacing: 0.2em;
    margin-left: 0.2em;
  }
  .card--front .wordmark__tag {
    font-size: 12px;
    letter-spacing: 0.4em;
    margin-top: 9px;
    margin-left: 0.4em;
  }

  .card--back .wordmark {
    left: 250px; width: 222px; top: 206px;
    color: var(--gold);
  }
  .card--back .wordmark__dot {
    width: 10px; height: 10px;
    background: var(--gold);
    margin-bottom: 12px;
  }
  .card--back .wordmark__name {
    font-size: 19px;
    letter-spacing: 0.14em;
    margin-left: 0.14em;
  }
  .card--back .wordmark__tag {
    font-size: 9.5px;
    letter-spacing: 0.38em;
    margin-top: 5px;
    margin-left: 0.38em;
  }

  /* Back side details */
  .edge-accent {
    position: absolute;
    left: -22px; top: 34px;
    width: 32px; height: 62px;
    border-radius: 0 31px 31px 0;
    background: var(--gold);
  }
  .holder {
    position: absolute;
    left: 23px; top: 44px;
    font-family: "Roboto", sans-serif;
  }
  .holder__name {
    font-size: 18px;
    font-weight: 700;
    color: var(--gold);
    line-height: 1.2;
  }
  .holder__role {
    font-size: 12px;
    color: var(--ink);
    margin-top: 4px;
  }
  .contacts {
    position: absolute;
    left: 22px; top: 176px;
    list-style: none;
    font-family: "Roboto", sans-serif;
    font-size: 12.5px;
    color: var(--ink);
  }
  .contacts li {
    display: flex;
    align-items: center;
    height: 18.4px;
  }
  .contacts svg {
    width: 11px; height: 11px;
    margin-right: 14px;
    flex: none;
  }
</style>
</head>
<body>
<main class="canvas">

  <section class="card card--front" aria-label="Card front">
    <div class="wordmark">
      <span class="wordmark__dot"></span>
      <span class="wordmark__name">Lewis Marrow</span>
      <span class="wordmark__tag">Wedding Films</span>
    </div>
  </section>

  <section class="card card--back" aria-label="Card back">
    <span class="edge-accent"></span>
    <div class="holder">
      <p class="holder__name">Lewis Marrow</p>
      <p class="holder__role">Managing Director</p>
    </div>

    <ul class="contacts">
      <li>
        <svg viewBox="0 0 12 12" aria-hidden="true"><path fill="#2b2b2b" d="M1 3.5C1 2 3 1 6 1s5 1 5 2.5v1H8.5V3.5h-5v1H1zM2.5 5.5h7L11 11H1z"/></svg>
        07312 605 227
      </li>
      <li>
        <svg viewBox="0 0 12 12" aria-hidden="true"><rect x="1" y="2.5" width="10" height="7" fill="#2b2b2b"/><path d="M1 2.5l5 4 5-4" fill="none" stroke="#f2f2f2" stroke-width="1"/></svg>
        films@lewismarrowreels.com
      </li>
      <li>
        <svg viewBox="0 0 12 12" aria-hidden="true"><g fill="none" stroke="#2b2b2b" stroke-width="1"><circle cx="6" cy="6" r="5"/><ellipse cx="6" cy="6" rx="2.2" ry="5"/><path d="M1 6h10M2 3.5h8M2 8.5h8"/></g></svg>
        www.lewismarrowreels.com
      </li>
      <li>
        <svg viewBox="0 0 12 12" aria-hidden="true"><circle cx="6" cy="6" r="5.5" fill="#2b2b2b"/></svg>
        @lewismarrowweddingfilms
      </li>
      <li>
        <svg viewBox="0 0 12 12" aria-hidden="true"><rect x="1" y="1" width="10" height="10" rx="2.5" fill="none" stroke="#2b2b2b" stroke-width="1.3"/></svg>
        @lewismarrowfilms
      </li>
    </ul>

    <div class="wordmark">
      <span class="wordmark__dot"></span>
      <span class="wordmark__name">Lewis Marrow</span>
      <span class="wordmark__tag">Wedding Films</span>
    </div>
  </section>

</main>
</body>
</html>
```